Billboard design 8x3M NURA (Spanish company)

We´re located in the south of Spain. We run a local telecom company.
We sell Fiber optic, and mobile phone lines mainly.
The billboard will have to be in Spanish, I would like the price to be something you spot on first sight when passing by in the car.
Our company color is blue, like in our logo which I will add. I will also add a example from what we currently have.
The new offer should be:
1000 megas + 100Gigas movil con llamadas ilimitadas. (meaning 1000Mb fiber optic speed and 100Gb data and unlimited calls for 1 mobile line)
Our details are: phone line 952 00 0147
Website: nu-ra.es

```html
<!DOCTYPE html>
<html lang="es">
<head>
<meta charset="utf-8">
<title>NURA – Valla 8x3</title>
<link href="https://fonts.googleapis.com/css2?family=Montserrat:wght@600;700;800&display=swap" rel="stylesheet">
<style>
  :root {
    --navy: #0d2c46;
    --blue-deep: #14507a;
    --blue-bright: #2288c4;
    --yellow: #f8c31d;
    --ink: #0b2a40;
    --white: #ffffff;
    --backdrop: #9c9c9c;
  }
  * { margin: 0; padding: 0; box-sizing: border-box; }
  html, body {
    width: 720px;
    height: 1200px;
    overflow: hidden;
    background: var(--backdrop);
    font-family: "Montserrat", sans-serif;
  }
  .billboard {
    position: absolute;
    left: 20px;
    top: 473px;
    width: 680px;
    height: 254px;
    background: var(--white);
    box-shadow: 14px 14px 22px rgba(0,0,0,0.35);
    overflow: hidden;
  }
  .billboard__hero {
    position: absolute;
    inset: 0 0 61px 0;
    background: linear-gradient(100deg, var(--navy) 0%, var(--blue-deep) 45%, var(--blue-bright) 100%);
  }
  .headline {
    position: absolute;
    left: 27px;
    top: 14px;
    font-weight: 800;
    font-size: 34px;
    line-height: 41px;
    letter-spacing: -0.5px;
  }
  .headline__accent { color: var(--yellow); display: block; }
  .headline__main { color: var(--white); display: block; }
  .offer {
    position: absolute;
    left: 27px;
    top: 100px;
    display: flex;
    align-items: flex-start;
    gap: 6px;
    font-weight: 800;
  }
  .offer__item { display: flex; flex-direction: column; line-height: 1; }
  .offer__value { color: var(--yellow); font-size: 33px; letter-spacing: -0.5px; }
  .offer__unit { color: var(--white); font-size: 23px; margin-top: -2px; padding-left: 3px; }
  .offer__plus { color: var(--white); font-size: 30px; margin-top: 16px; }
  .offer__calls {
    position: absolute;
    left: 29px;
    top: 163px;
    color: var(--white);
    font-weight: 700;
    font-size: 15px;
    line-height: 18px;
  }
  .offer__calls strong { color: var(--yellow); font-weight: 800; }
  .price {
    position: absolute;
    left: 264px;
    top: 104px;
    width: 112px;
    height: 62px;
    background: var(--yellow);
    border-radius: 4px;
    color: var(--ink);
    text-align: center;
    font-weight: 800;
  }
  .price__label { display: block; font-size: 13px; line-height: 13px; padding-top: 5px; }
  .price__amount { display: block; font-size: 38px; line-height: 40px; letter-spacing: -1px; }
  .brand {
    position: absolute;
    left: 508px;
    top: 16px;
    color: var(--white);
  }
  .brand__name { display: block; font-size: 40px; font-weight: 800; letter-spacing: 2px; line-height: 44px; }
  .brand__services { display: block; font-size: 11.5px; font-weight: 600; margin-top: 3px; }
  .illustration {
    position: absolute;
    left: 430px;
    top: 92px;
    width: 225px;
    height: 144px;
    border-radius: 24px;
    background: linear-gradient(160deg, #f2f5f9 0%, #2c64bd 35%, #1c4fa8 65%, #e9eef4 100%);
  }
  .contact {
    position: absolute;
    left: 30px;
    bottom: 16px;
    display: flex;
    align-items: center;
    gap: 6px;
    color: var(--ink);
    font-weight: 700;
    font-size: 23px;
    letter-spacing: -0.3px;
  }
  .contact__icon { width: 15px; height: 15px; flex: none; }
  .contact__web { margin-left: 4px; }
</style>
</head>
<body>
  <section class="billboard">
    <div class="billboard__hero"></div>

    <h1 class="headline">
      <span class="headline__accent">TU FIBRA + MÓVIL</span>
      <span class="headline__main">AL MEJOR PRECIO</span>
    </h1>

    <div class="offer">
      <div class="offer__item"><span class="offer__value">1000</span><span class="offer__unit">megas</span></div>
      <span class="offer__plus">+</span>
      <div class="offer__item"><span class="offer__value">100</span><span class="offer__unit">Gigas</span></div>
    </div>
    <p class="offer__calls">con <strong>llamadas ilimitadas</strong></p>

    <div class="price">
      <span class="price__label">POR</span>
      <span class="price__amount">35€</span>
    </div>

    <div class="brand">
      <span class="brand__name">NURA</span>
      <span class="brand__services">Wifi | Fibra | Movil | Tv</span>
    </div>

    <div class="illustration" role="img" aria-label="Ilustración de un cohete azul y rojo saliendo de la pantalla de un portátil con una estela blanca"></div>

    <div class="contact">
      <svg class="contact__icon" viewBox="0 0 16 16" aria-hidden="true">
        <circle cx="8" cy="8" r="8" fill="#f8c31d"/>
        <path d="M5.2 4.2l1.4-.3.8 2-1 .7c.5 1.1 1.3 1.9 2.4 2.4l.7-1 2 .8-.3 1.4c-3.4.3-6.3-2.6-6-6z" fill="#0b2a40"/>
      </svg>
      <span class="contact__phone">952 00 0147</span>
      <svg class="contact__icon" viewBox="0 0 16 16" aria-hidden="true">
        <circle cx="8" cy="8" r="8" fill="#f8c31d"/>
        <g fill="none" stroke="#0b2a40" stroke-width="1">
          <circle cx="8" cy="8" r="4.5"/>
          <ellipse cx="8" cy="8" rx="2" ry="4.5"/>
          <line x1="3.5" y1="8" x2="12.5" y2="8"/>
        </g>
      </svg>
      <span class="contact__web">www.nu-ra.es</span>
    </div>
  </section>
</body>
</html>
```